High End Business Card Design for Flooring Store

Looking for a new card design for our hardwood flooring company. We have no print budget for these and are open to cards made from wood, metal, cardstock with embossed print ... or any combination of these. No plastic.

We sell luxury products and I want the cards to reflect our image of quality and class.

Our contact information as such;
Employee Name
418 Colbrook Blvd.
Marlow, ON
K9R-3M5
(555) 214-3968
Employee email @velkaflooring.com

Target Market(s)

Home Builders

Contact Information for Business Card

Emnployee name, business contact information

```html
<!DOCTYPE html>
<html lang="en">
<head>
<meta charset="utf-8">
<title>Velka Flooring – Business Card</title>
<link rel="stylesheet" href="https://fonts.googleapis.com/css2?family=Montserrat:wght@400;500&family=Archivo+Narrow:wght@600&family=Roboto:wght@400&display=swap">
<style>
  :root {
    --backdrop: #a7a7a7;
    --wood-light: #f6e8c3;
    --wood-mid: #efdcaa;
    --wood-warm: #f2deae;
    --brand-red: #8e2a22;
    --brand-gold: #e9b526;
    --tagline-grey: #6c6865;
  }
  * { margin: 0; padding: 0; box-sizing: border-box; }
  html, body { width: 1200px; height: 1153px; overflow: hidden; }
  body {
    background: var(--backdrop);
    position: relative;
    font-family: "Montserrat", sans-serif;
  }
  .card {
    position: absolute;
    top: 416px;
    width: 560px;
    height: 320px;
    overflow: hidden;
  }
  .card--front { left: 30px; }
  .card--back { left: 610px; }
  .card__wood {
    position: absolute;
    inset: 0;
    background: linear-gradient(100deg, var(--wood-light) 0%, var(--wood-warm) 35%, var(--wood-mid) 60%, var(--wood-light) 100%);
  }
  /* Front */
  .brand {
    position: absolute;
    left: 0; right: 0;
    top: 104px;
    text-align: center;
  }
  .brand__name {
    display: inline-flex;
    align-items: center;
    gap: 12px;
    font-size: 72px;
    font-weight: 500;
    color: var(--brand-red);
    line-height: 1;
  }
  .brand__mark {
    width: 34px; height: 34px;
    background: var(--brand-gold);
  }
  .brand__tagline {
    margin-top: 4px;
    font-size: 17px;
    font-weight: 400;
    color: var(--tagline-grey);
    line-height: 1.2;
  }
  /* Back */
  .employee-name {
    position: absolute;
    left: 40px; top: 34px;
    font-size: 25px;
    font-weight: 500;
    color: var(--brand-red);
    letter-spacing: 0.3px;
  }
  .phone {
    position: absolute;
    right: 36px; top: 114px;
    display: flex; align-items: center; gap: 10px;
    font-family: "Roboto", sans-serif;
    font-size: 14px;
    color: var(--brand-red);
  }
  .address-band {
    position: absolute;
    left: 0; right: 0;
    top: 142px; height: 71px;
    background: var(--brand-gold);
  }
  .address {
    position: absolute;
    left: 42px; top: 150px;
    font-family: "Archivo Narrow", sans-serif;
    font-weight: 600;
    font-size: 12.5px;
    line-height: 19.5px;
    color: var(--brand-red);
    font-style: normal;
  }
  .address__line { display: flex; align-items: center; padding-left: 15px; }
  .address__line--first { padding-left: 0; gap: 6px; }
  .email {
    position: absolute;
    left: 190px; top: 277px;
    font-size: 12px;
    letter-spacing: 2px;
    color: var(--brand-red);
  }
</style>
</head>
<body>
  <section class="card card--front" aria-label="Card front">
    <div class="card__wood" role="img" aria-label="Light maple wood veneer surface"></div>
    <div class="brand">
      <div class="brand__name"><span class="brand__mark"></span>Velka</div>
      <p class="brand__tagline">Planchers &amp; Escaliers<br>Flooring &amp; Stairs</p>
    </div>
  </section>

  <section class="card card--back" aria-label="Card back">
    <div class="card__wood" role="img" aria-label="Light maple wood veneer surface"></div>
    <h1 class="employee-name">Employee Name</h1>
    <div class="phone">
      <span>(555) 214-3968</span>
      <svg width="7" height="11" viewBox="0 0 7 11" aria-hidden="true">
        <rect x="0.6" y="0.6" width="5.8" height="9.8" rx="1" fill="none" stroke="currentColor" stroke-width="1.2"/>
        <line x1="2.5" y1="8.6" x2="4.5" y2="8.6" stroke="currentColor" stroke-width="1"/>
      </svg>
    </div>
    <div class="address-band"></div>
    <address class="address">
      <span class="address__line address__line--first">
        <svg width="9" height="10" viewBox="0 0 9 10" aria-hidden="true">
          <circle cx="4.5" cy="3.2" r="2.4" fill="none" stroke="currentColor" stroke-width="1.3"/>
          <path d="M4.5 5.6 V8.4 M1 9.2 H8" stroke="currentColor" stroke-width="1.3"/>
        </svg>
        418 Colbrook Blvd.
      </span>
      <span class="address__line">K9R-3M5</span>
      <span class="address__line">Marlow, ON</span>
    </address>
    <p class="email">@velkaflooring.com</p>
  </section>
</body>
</html>
```